Career Ad - Graphic Image to Attract New Team Members to our Company

We would like a career ad to be used for recruiting staff. This ad will be posted through our social media sites and may also be printed on post cards. Concept we like so far (however we are open to other creative ideas) is a photo in the background with printing on top. The color would be our brand color : blue. As for content, words like "We're Hiring" or "Come join our team" we'd also like to have reference to our website https://brindlecove.ca/about/careers and our email careers@brindlecove.ca Of course, our logo and company name, which is attached in the files
Professional
- company logo
- visually apealling

```html
<!DOCTYPE html>
<html lang="en">
<head>
<meta charset="utf-8">
<title>Brindle Cove Brokers – We Are Hiring</title>
<link rel="stylesheet" href="https://fonts.googleapis.com/css2?family=Oswald:wght@500&family=Tinos&family=Arimo:wght@400;700&family=Libre+Baskerville:wght@700&display=swap">
<style>
  :root {
    --brand-navy: #1b3a8c;
    --brand-blue: #1a3f9a;
    --headline-grey: #3b3b3b;
    --contact-grey: #2e2e2e;
    --white: #ffffff;
    --wall-light: #d2d2d0;
    --wall-mid: #a9a9a7;
    --wall-dark: #5e5e5c;
    --floor: #4d4d4b;
  }
  html, body {
    margin: 0;
    padding: 0;
    width: 1200px;
    height: 628px;
    overflow: hidden;
    background: var(--wall-mid);
  }
  .ad {
    position: relative;
    width: 1200px;
    height: 628px;
    overflow: hidden;
  }
  .ad__scene {
    position: absolute;
    inset: 0;
    background:
      radial-gradient(ellipse 60% 45% at 85% 58%, rgba(140, 170, 200, 0.35), rgba(140, 170, 200, 0) 70%),
      linear-gradient(180deg, rgba(0,0,0,0) 86%, var(--floor) 100%),
      radial-gradient(ellipse 75% 70% at 45% 45%, var(--wall-light) 0%, var(--wall-mid) 60%, var(--wall-dark) 100%);
  }
  .brand {
    position: absolute;
    left: 22px;
    top: 44px;
    display: flex;
    align-items: center;
    gap: 18px;
  }
  .brand__mark {
    width: 78px;
    height: 78px;
    background: var(--brand-navy);
  }
  .brand__name {
    font-family: "Libre Baskerville", serif;
    font-weight: 700;
    font-size: 34px;
    line-height: 1.15;
    color: var(--brand-navy);
    letter-spacing: 1px;
    margin: 0;
  }
  .info-button {
    position: absolute;
    left: 776px;
    top: 40px;
    width: 404px;
    height: 68px;
    border-radius: 6px;
    background: var(--brand-blue);
    color: var(--white);
    font-family: "Arimo", sans-serif;
    font-weight: 700;
    font-size: 24px;
    display: flex;
    align-items: center;
    padding-left: 13px;
    box-sizing: border-box;
    text-decoration: none;
    gap: 8px;
  }
  .info-button__icon {
    width: 42px;
    height: 50px;
  }
  .contact {
    position: absolute;
    right: 20px;
    top: 116px;
    margin: 0;
    font-family: "Arimo", sans-serif;
    font-weight: 700;
    font-size: 16px;
    line-height: 1.4;
    color: var(--contact-grey);
    text-align: right;
  }
  .headline {
    position: absolute;
    margin: 0;
    font-family: "Oswald", sans-serif;
    font-weight: 500;
    color: var(--headline-grey);
    text-transform: uppercase;
    line-height: 1;
    white-space: nowrap;
  }
  .headline--first {
    left: 120px;
    top: 169px;
    font-size: 80px;
    letter-spacing: 1px;
  }
  .headline--second {
    left: 18px;
    top: 247px;
    font-size: 80px;
    letter-spacing: 0.5px;
  }
  .hiring {
    margin: 0;
    font-family: "Tinos", serif;
    font-weight: 400;
    color: var(--white);
    line-height: 1;
    white-space: nowrap;
  }
  .hiring__lead,
  .hiring__word {
    position: absolute;
    transform-origin: left top;
  }
  .hiring__lead {
    left: 345px;
    top: 507px;
    font-size: 78px;
    transform: scaleX(0.74);
  }
  .hiring__word {
    left: 570px;
    top: 459px;
    font-size: 174px;
    transform: scaleX(0.9);
  }
</style>
</head>
<body>
  <main class="ad">
    <div class="ad__scene" role="img" aria-label="Photo of a businessman in a suit standing before a grey concrete wall with chalk-drawn staircase of colourful charts and success doodles rising to the right"></div>

    <div class="brand">
      <div class="brand__mark"></div>
      <p class="brand__name">BRINDLE COVE<br>BROKERS</p>
    </div>

    <a class="info-button" href="https://brindlecove.ca/about/careers">
      Click Here For More Info
      <svg class="info-button__icon" viewBox="0 0 42 50" aria-hidden="true" fill="none" stroke="#ffffff" stroke-width="2.4" stroke-linecap="round" stroke-linejoin="round">
        <path d="M16 8 V2 M8 11 L4 7 M24 11 L28 7"/>
        <path d="M13 30 V16 a3 3 0 0 1 6 0 V27 M19 25 a3 3 0 0 1 6 0 V28 M25 27 a3 3 0 0 1 6 0 V30 M31 29 a3 3 0 0 1 6 0 V38 c0 6-4 10-10 10 h-5 c-4 0-6-2-8-5 L8 34 a3 3 0 0 1 5-4 l0 0"/>
      </svg>
    </a>

    <p class="contact">brindlecove.ca/about/careers<br>careers@brindlecove.ca</p>

    <h1 class="headline headline--first">Looking for a</h1>
    <p class="headline headline--second">Career Opportunity?</p>

    <p class="hiring"><span class="hiring__lead">WE ARE</span><span class="hiring__word">HIRING!</span></p>
  </main>
</body>
</html>
```